Webdesign für Vermietung eines Ferienhauses auf der Insel Usedom
Zielgruppe
Vermietung eines Ferienhauses auf der Insel Usedom
ZG: Urlauber im gehobenem Preissegment, die Luxus schätzen und urlauben wollen
Aufgabenstellung
- IN ADOBE PHOTOSHOP
- Bilder können hier entnommen werden: https://www.quartiro-net.example/ob-link-ansicht-reserve/index.php?portal=48127&unit=39502/index.html
- gern können Sie auch Stock-Bilder verwenden
- Der Buchungskalender /die Verfügbarkeit der freien Zeiträume soll präsent im oberen Bereich der Seite stehen
- Lumivo-Bewertungsbutton
- Es gibt kein Logo - bitte den Namenszug 'KIEFERNVILLA*****HOLMSTEDE' nutzen

```html
<!DOCTYPE html>
<html lang="de">
<head>
<meta charset="utf-8">
<title>Kiefernvilla Holmstede</title>
<link href="https://fonts.googleapis.com/css2?family=Lato:wght@400;700&display=swap" rel="stylesheet">
<style>
:root{
  --green:#7fba00;
  --cal-free:#8ee88e;
  --cal-busy:#ffb3c0;
  --dark:#4a4a4a;
  --text:#444;
  --muted:#777;
  --line:#d9d9d9;
  --field:#f4f4f4;
  --footer:#555;
  --ink:#2b2b2b;
}
*{box-sizing:border-box;margin:0;padding:0}
html,body{width:722px;height:1200px;overflow:hidden;background:#fff}
body{font-family:'Lato',sans-serif;color:var(--text);position:relative}
.abs{position:absolute}

.site-header{left:0;top:0;width:722px;height:37px;background:#fff}
.brand{left:90px;top:12px;display:flex;align-items:center;gap:5px;font-weight:700;font-size:11px;color:var(--ink);white-space:nowrap}
.brand i{display:block;width:8px;height:8px;background:var(--green)}
.main-nav{top:14px;left:0;width:722px;font-size:7px;font-weight:700;color:#333}
.main-nav span{position:absolute;white-space:nowrap}

.hero{left:0;top:37px;width:722px;height:295px;
  background:radial-gradient(ellipse at 50% 40%,#8c9a7a 0%,transparent 35%),
             linear-gradient(120deg,#3f6b2a 0%,#5f8a3d 35%,#7c9166 55%,#5e8a3e 75%,#8a9a88 100%)}
.hero-dots{left:342px;top:203px;display:flex;gap:4px}
.hero-dots i{width:5px;height:5px;border-radius:50%;background:#fff;display:block}
.hero-dots i:first-child{background:var(--green)}

.booking{left:159px;top:274px;width:402px;height:299px;background:#fff;box-shadow:0 0 4px rgba(0,0,0,.18)}
.booking-title{left:0;top:0;width:402px;height:24px;background:var(--green);color:#fff;font-weight:700;font-size:8.4px;text-align:center;line-height:24px}
.field{height:21px;background:var(--field);border:1px solid #dcdcdc;font-size:7px;color:var(--muted);padding-left:8px;line-height:19px}
.field svg{position:absolute;right:7px;top:5px}
.check-btn{left:270px;top:59px;width:122px;height:21px;background:var(--green);color:#fff;font-weight:700;font-size:7px;text-align:center;line-height:21px}

.month{width:122px}
.month-name{text-align:center;font-size:7px;color:#333;height:10px;line-height:10px}
.cal{border-collapse:collapse;width:122px;table-layout:fixed}
.cal th{background:#e6e6e6;font-size:6.4px;font-weight:700;color:#333;height:18px;border:1px solid var(--line)}
.cal td{height:17.5px;font-size:6.4px;text-align:center;border:1px solid var(--line);color:var(--muted);background:#fff}
.cal td.g{background:var(--cal-free);color:#222}
.cal td.p{background:var(--cal-busy);color:#222}
.cal td.a{background:linear-gradient(135deg,var(--cal-busy) 50%,var(--cal-free) 50%);color:#222}
.cal td.d{background:linear-gradient(135deg,var(--cal-free) 50%,var(--cal-busy) 50%);color:#222}
.cal td.b{font-weight:700}
.cal tr.spacer td{height:17px;border-left:none;border-right:none;border-bottom:1px solid var(--line)}
.cal-frame{border-left:1px solid var(--line);border-right:1px solid var(--line)}

.legend{left:8px;top:242px;display:flex;align-items:center;gap:3px;font-size:4.6px;color:#333;background:#f5f5f5;padding:2px 3px}
.legend i{width:6px;height:6px;display:inline-block;margin-right:2px}
.legend span{margin-right:3px;display:flex;align-items:center}
.submit{left:149px;top:266px;width:106px;height:22px;background:var(--dark);color:#fff;font-weight:700;font-size:7.2px;text-align:center;line-height:22px;border-radius:1px}

.house-card{left:83px;top:611px;width:543px;height:160px;border:1px solid #ddd}
.house-head{left:0;top:0;width:541px;height:26px;background:var(--green);color:#fff;font-weight:700;font-size:7.4px;line-height:26px;padding-left:15px}
.house-photo{left:16px;top:40px;width:155px;height:103px;background:linear-gradient(135deg,#e8e6e2,#b9b6b0 60%,#7c7a76)}
.house-text{left:187px;top:43px;width:336px;font-size:7px;line-height:10.8px;color:#555}
.more-btn{left:187px;top:124px;width:91px;height:19px;background:var(--dark);color:#fff;font-weight:700;font-size:6.8px;text-align:center;line-height:19px;border-radius:1px}

.stars{left:250px;top:795px}
.title{left:171px;top:807px;width:200px;text-align:center;font-weight:700;font-size:15.6px;color:#333}
.address{left:171px;top:829px;width:200px;text-align:center;font-size:7.2px;color:#222}

.gallery-main{left:84px;top:855px;width:375px;height:196px;background:linear-gradient(180deg,#7fa6cf 0%,#a9c4de 30%,#efefef 55%,#c8c8c8 80%,#6f6a5e 100%)}
.g-arrow{width:22px;height:22px;border-radius:50%;background:var(--green)}
.thumb{top:1056px;width:50px;height:37px}
.thumb-arrow{left:464px;top:1067px;width:14px;height:14px;border-radius:50%;background:#eee}

.info{left:495px;top:855px;width:134px}
.info h2{font-size:8px;font-weight:700;color:#111;margin-bottom:9px}
.info p{font-size:7px;line-height:10.85px;color:#555}

.rating-btn{left:495px;top:1068px;width:128px;height:22px;border:1px solid #ccc;border-radius:11px;background:#fff;display:flex;align-items:center;justify-content:center;gap:5px;font-size:7px;font-weight:700;color:#333}

.site-footer{left:0;top:1154px;width:722px;height:46px;background:var(--footer);color:#fff;font-size:7px;font-weight:700;text-align:center;line-height:46px}
</style>
</head>
<body>

<header class="site-header abs">
  <div class="brand abs"><i></i>Kiefernvilla Holmstede</div>
  <nav class="main-nav abs">
    <span style="left:309px">DAS 5* STRANDHAUS</span>
    <span style="left:397px">VERFÜGBARKEIT</span>
    <span style="left:472px">DIE RÄUMLICHKEITEN</span>
    <span style="left:563px">LAGE</span>
    <span style="left:597px">KONTAKT</span>
  </nav>
</header>

<div class="hero abs" role="img" aria-label="Luftaufnahme der Ferienhausanlage mit Reetdachhäusern im Kiefernwald">
  <div class="hero-dots abs"><i></i><i></i><i></i><i></i><i></i></div>
</div>

<section class="booking abs">
  <div class="booking-title abs">Verfügbarkeit prüfen</div>
  <div class="field abs" style="left:10px;top:32px;width:122px">16.11.2022
    <svg width="10" height="10" viewBox="0 0 10 10"><rect x=".5" y="1.5" width="9" height="8" fill="none" stroke="#888"/><path d="M.5 3.5h9M3 .5v2M7 .5v2" stroke="#888"/><g fill="#888"><rect x="2" y="5" width="1" height="1"/><rect x="4.5" y="5" width="1" height="1"/><rect x="7" y="5" width="1" height="1"/><rect x="2" y="7" width="1" height="1"/><rect x="4.5" y="7" width="1" height="1"/><rect x="7" y="7" width="1" height="1"/></g></svg>
  </div>
  <div class="field abs" style="left:140px;top:32px;width:122px">2 Erw.</div>
  <div class="field abs" style="left:10px;top:59px;width:122px">17.11.2022
    <svg width="10" height="10" viewBox="0 0 10 10"><rect x=".5" y="1.5" width="9" height="8" fill="none" stroke="#888"/><path d="M.5 3.5h9M3 .5v2M7 .5v2" stroke="#888"/><g fill="#888"><rect x="2" y="5" width="1" height="1"/><rect x="4.5" y="5" width="1" height="1"/><rect x="7" y="5" width="1" height="1"/><rect x="2" y="7" width="1" height="1"/><rect x="4.5" y="7" width="1" height="1"/><rect x="7" y="7" width="1" height="1"/></g></svg>
  </div>
  <div class="field abs" style="left:140px;top:59px;width:122px">Kind(er)</div>
  <div class="check-btn abs">Jetzt prufen</div>

  <div class="month abs" style="left:10px;top:97px">
    <div class="month-name">November 2022</div>
    <table class="cal cal-frame">
      <tr><th>Su</th><th>Mo</th><th>Tu</th><th>We</th><th>Th</th><th>Fr</th><th>Sa</th></tr>
      <tr><td></td><td></td><td>1</td><td>2</td><td>3</td><td>4</td><td>5</td></tr>
      <tr><td>6</td><td>7</td><td>8</td><td>9</td><td>10</td><td>11</td><td>12</td></tr>
      <tr><td>13</td><td>14</td><td>15</td><td>16</td><td>17</td><td class="g b">18</td><td class="g">19</td></tr>
      <tr><td class="g">20</td><td class="g">21</td><td class="g">22</td><td class="g">23</td><td class="g">24</td><td class="g">25</td><td class="g">26</td></tr>
      <tr><td class="g">27</td><td class="g">28</td><td class="g">29</td><td class="g">30</td><td></td><td></td><td></td></tr>
      <tr class="spacer"><td colspan="7"></td></tr>
    </table>
  </div>

  <div class="month abs" style="left:140px;top:97px">
    <div class="month-name">Dezember2022</div>
    <table class="cal cal-frame">
      <tr><th>Su</th><th>Mo</th><th>Tu</th><th>We</th><th>Th</th><th>Fr</th><th>Sa</th></tr>
      <tr><td></td><td></td><td></td><td></td><td class="g">1</td><td class="g">2</td><td class="g">3</td></tr>
      <tr><td class="g">4</td><td class="g">5</td><td class="g">6</td><td class="g">7</td><td class="g">8</td><td class="g">9</td><td class="g">10</td></tr>
      <tr><td class="g">11</td><td class="g">12</td><td class="g">13</td><td class="g">14</td><td class="g">15</td><td class="g">16</td><td class="g">17</td></tr>
      <tr><td class="g">18</td><td class="g">19</td><td class="d">20</td><td class="p">21</td><td class="p">22</td><td class="p">23</td><td class="p">24</td></tr>
      <tr><td class="p">25</td><td class="p">26</td><td class="p">27</td><td class="p">28</td><td class="p">29</td><td class="p">30</td><td class="p">31</td></tr>
      <tr class="spacer"><td colspan="7"></td></tr>
    </table>
  </div>

  <div class="month abs" style="left:270px;top:97px">
    <div class="month-name">Januar2023</div>
    <table class="cal cal-frame">
      <tr><th>Su</th><th>Mo</th><th>Tu</th><th>We</th><th>Th</th><th>Fr</th><th>Sa</th></tr>
      <tr><td class="p">1</td><td class="p">2</td><td class="p">3</td><td class="p">4</td><td class="p">5</td><td class="p">6</td><td class="p">7</td></tr>
      <tr><td class="p">8</td><td class="p">9</td><td class="p">10</td><td class="a">11</td><td class="g">12</td><td class="g">13</td><td class="g">14</td></tr>
      <tr><td class="g">15</td><td class="g">16</td><td class="g">17</td><td class="g">18</td><td class="g">19</td><td class="g">20</td><td class="g">21</td></tr>
      <tr><td class="g">22</td><td class="g">23</td><td class="g">24</td><td class="g">25</td><td class="g">26</td><td class="g">27</td><td class="g">28</td></tr>
      <tr><td class="g">29</td><td class="g">30</td><td class="g">31</td><td></td><td></td><td></td><td></td></tr>
      <tr class="spacer"><td colspan="7"></td></tr>
    </table>
  </div>

  <div class="legend abs">
    <span><i style="background:var(--cal-busy)"></i>nicht verfügbar</span>
    <span><i style="background:var(--cal-free)"></i>verfügbar</span>
    <span><i style="background:linear-gradient(135deg,var(--cal-busy) 50%,var(--cal-free) 50%)"></i>möglicher Anreisetag</span>
    <span><i style="background:linear-gradient(135deg,var(--cal-free) 50%,var(--cal-busy) 50%)"></i>möglicher Abreisetag</span>
  </div>
  <div class="submit abs">Verfügbarkeit prüfen</div>
</section>

<section class="house-card abs">
  <div class="house-head abs">Haus 30d (5*)</div>
  <div class="house-photo abs" role="img" aria-label="Heller Wohn- und Essbereich mit gedecktem Tisch"></div>
  <div class="house-text abs">
    5-Sterne-Klassifizierung durch den Nordischen Gästeverband<br>
    Haustiere sind weder im Haus noch auf dem Grundstück zulässig.<br>
    -<br>
    Um unserem hohen Anspruch an Sauberkeit in diesen großen Strandhäusern gerecht werden zu können,<br>sind wir dazu gezwungen, die Objekte in der Kernzeit der Hauptsaison in einem gewissen Rhythmus zu<br>vermieten. Dieses Objekt kann somit vom 28.06.23 bis 30.08.23 nur von Mittwoch zu Mittwoch gemietet<br>werden.
  </div>
  <div class="more-btn abs">mehr informationen</div>
</section>

<svg class="stars abs" width="45" height="9" viewBox="0 0 45 9" aria-label="5 Sterne">
  <g fill="#f5c400">
    <path id="st" d="M4.5 0l1.3 2.9 3.1.3-2.4 2.1.7 3.1-2.7-1.6-2.7 1.6.7-3.1L.1 3.2l3.1-.3z"/>
    <use href="#st" x="9"/><use href="#st" x="18"/><use href="#st" x="27"/><use href="#st" x="36"/>
  </g>
</svg>
<h1 class="title abs">Das 5* Strandhaus</h1>
<div class="address abs">Holmstede - Dünenweg 30d (5*) &nbsp;-&nbsp; 1 F</div>

<div class="gallery-main abs" role="img" aria-label="Weißes Strandhaus mit Reetdach und Terrasse unter blauem Himmel"></div>
<div class="g-arrow abs" style="left:72px;top:942px"><svg width="22" height="22"><path d="M13 7l-4 4 4 4" fill="none" stroke="#fff" stroke-width="1.3"/></svg></div>
<div class="g-arrow abs" style="left:449px;top:942px"><svg width="22" height="22"><path d="M9 7l4 4-4 4" fill="none" stroke="#fff" stroke-width="1.3"/></svg></div>

<div class="thumb abs" style="left:84px;background:linear-gradient(#6f9acb,#dcdcdc 60%,#5c7a3e)" role="img" aria-label="Haus von außen"></div>
<div class="thumb abs" style="left:139px;background:linear-gradient(#1d2b5a,#3c4f86 60%,#222)" role="img" aria-label="Haus am Abend beleuchtet"></div>
<div class="thumb abs" style="left:193px;background:linear-gradient(#1a0b0b,#a8151b 55%,#1a0b0b)" role="img" aria-label="Whirlpool mit roter Beleuchtung"></div>
<div class="thumb abs" style="left:248px;background:linear-gradient(#0e3b3a,#2fb3a8 55%,#0f2a2a)" role="img" aria-label="Whirlpool mit türkiser Beleuchtung"></div>
<div class="thumb abs" style="left:302px;background:linear-gradient(#7da4cf,#e9e9e9 55%,#6f8a4d)" role="img" aria-label="Hausansicht mit Garten"></div>
<div class="thumb abs" style="left:356px;background:linear-gradient(#8c6b4a,#c9b89e 55%,#6d5c48)" role="img" aria-label="Terrasse mit Gartenmöbeln"></div>
<div class="thumb abs" style="left:411px;background:linear-gradient(#5c4a3a,#8a7a66 55%,#3d8f88)" role="img" aria-label="Terrasse mit Sitzgruppe"></div>
<div class="thumb-arrow abs"><svg width="14" height="14"><path d="M6 4.5l2.5 2.5L6 9.5" fill="none" stroke="#555" stroke-width="1"/></svg></div>

<aside class="info abs">
  <h2>Allgemeine Informationen</h2>
  <p>"MERIDA Küstenland" in Holmstede ist eine in Mecklenburg-Vorpommern einzi­gartige 5-Sterne-Ferienhaus-Anlage mit 42 großzügigen, schilfrohrgedeckten Strandhäusern mit bis zu 225 m² Wohn­fläche und 26 Ferienwohnungen. Grund­stücke mit bis zu 3300 m² Fläche bieten viel Platz zum Wohlfühlen. Dieses exklu­sive, 2017 erbaute Strandhaus mit ca. 145 m² Wohnfläche und einem Grund­stück von ca. 700 m² befindet sich ca. 5 Gehminuten vom Strand entfernt.<br>Das Haus verfügt über beheizbarer Aus­senwhirlpool (ganzjährig nutzbar), Safe, Internet - WLAN, Sauna mit Infrarot, 2 Terrassen, HWR mit Waschmaschine und Trockner, Bollerwagen, Parkplatz.</p>
</aside>

<div class="rating-btn abs">
  <svg width="9" height="9" viewBox="0 0 9 9"><path d="M4.5 0l1.3 2.9 3.1.3-2.4 2.1.7 3.1-2.7-1.6-2.7 1.6.7-3.1L.1 3.2l3.1-.3z" fill="#f5c400"/></svg>
  Bewerten Sie uns auf Lumivo
</div>

<footer class="site-footer abs">© 2022 NV Buchungssysteme | Impressum | Datenschutz</footer>

</body>
</html>
```